Website for our 3rd party logistics warehouse company

Our company is a 3rd party logistics company. We receive and ship other businesses products for them. We offer our services to other smaller businesses that do not have a warehouse to operate out of. We also help many Brindlemart businesses prepare their products to be sold on Brindlemart.

We are looking for a modern looking design for our website. Please see our attached logo for design ideas. We are open to changing logo colors for website.

We really like the look of the website www.quorvela.com

Target Market(s)

Other businesses and brands of products

Industry/Entity Type

Warehousing and shipping

Number of Pages Required

2 page

Requirements
Must have
• We need 2 pages. Our main landing page and a duplicate page with different information geared towards brands.
Nice to have
• I like the look of overlay/transparent sections. Please see quorvela.com there is a ribbon that shows "Partners".

```html
<!DOCTYPE html>
<html lang="en">
<head>
<meta charset="utf-8">
<title>Vantor 3PL — Logistics Made Simple</title>
<link href="https://fonts.googleapis.com/css2?family=Poppins:wght@300;400;500;600;700&display=swap" rel="stylesheet">
<style>
:root{
  --yellow:#f8c71d;
  --yellow-deep:#e9b40f;
  --ink:#1b1b1b;
  --dark:#222222;
  --dark-2:#2d2d2d;
  --paper:#ffffff;
  --mist:#f1f1f1;
  --field:#ececec;
  --field-line:#dcdcdc;
  --muted:#8a8a8a;
  --font:'Poppins',sans-serif;
}
*{box-sizing:border-box;margin:0;padding:0}
html,body{width:1200px;height:4307px;overflow:hidden}
body{position:relative;font-family:var(--font);color:var(--ink);background:var(--paper)}
.abs{position:absolute}
.img-fill{position:absolute;inset:0}

/* header + hero */
.hero{position:absolute;left:0;top:0;width:1200px;height:637px;background:var(--mist)}
.hero__topwhite{position:absolute;left:0;top:0;width:450px;height:87px;background:var(--paper)}
.hero__yellow{position:absolute;left:450px;top:0;width:750px;height:637px;background:var(--yellow)}
.brand{font-family:var(--font);font-weight:600;letter-spacing:2px;white-space:nowrap}
.header__brand{left:62px;top:30px;font-size:17px;color:var(--ink)}
.header__call{left:918px;top:18px;display:flex;align-items:center;gap:14px}
.call__icon{width:38px;height:38px;border-radius:50%;background:var(--paper);display:flex;align-items:center;justify-content:center}
.call__label{font-size:9px;color:var(--paper);letter-spacing:1px;line-height:1}
.call__number{font-size:14px;font-weight:600;color:var(--ink);line-height:1.4}
.menu{left:1118px;top:22px;width:24px}
.menu span{display:block;height:3px;background:var(--ink);margin-bottom:5px}
.hero__photo{left:0;top:87px;width:637px;height:448px;background:linear-gradient(160deg,#3b5d8c 0%,#6a6f86 35%,#c56b3a 60%,#f0a34a 72%,#4b3b39 100%)}
.hero__kicker{left:665px;top:176px;font-size:13px;color:var(--paper);letter-spacing:1px}
.hero__title{left:665px;top:210px;font-size:50px;line-height:64px;font-weight:600;letter-spacing:-0.5px;color:var(--ink)}
.hero__text{left:665px;top:356px;width:456px;font-size:12.5px;line-height:21px;color:var(--paper)}
.btn{position:absolute;display:flex;align-items:center;justify-content:center;font-size:13px;font-weight:700;letter-spacing:.3px}
.btn--light{left:665px;top:440px;width:134px;height:36px;background:var(--paper);color:var(--ink)}
.btn--dark{left:820px;top:440px;width:136px;height:36px;background:var(--ink);color:var(--yellow)}
.hero__pager{left:1125px;font-size:11px;line-height:12px;width:16px;text-align:center;color:var(--ink)}

/* benefit */
.benefit{position:absolute;left:0;top:637px;width:1200px;height:982px;background:var(--paper)}
.ghost{position:absolute;font-weight:700;color:transparent;-webkit-text-stroke:1.5px rgba(0,0,0,.08);white-space:nowrap;line-height:1}
.ghost--light{-webkit-text-stroke:1.5px rgba(255,255,255,.10)}
.benefit__ghost{left:243px;top:132px;font-size:86px}
.benefit__title{left:0;width:796px;top:150px;text-align:center;font-size:27px;font-weight:700}
.benefit__sub{left:0;width:796px;top:222px;text-align:center;font-size:19px;font-weight:600;letter-spacing:1px}
.tile{position:absolute;width:300px;height:300px;overflow:hidden}
.tile--wide{width:600px}
.tile__num{position:absolute;left:48px;top:76px;font-size:68px;font-weight:500;line-height:1;color:transparent;-webkit-text-stroke:2px var(--yellow)}
.tile--yellow .tile__num{-webkit-text-stroke:2px rgba(40,30,0,.55)}
.tile__text{position:absolute;left:42px;top:160px;width:180px;font-size:14px;line-height:22px;color:var(--paper)}
.tile--yellow .tile__text{color:var(--ink)}
.tile__intro{position:absolute;left:20px;top:104px;width:262px;font-size:12px;line-height:20px;color:var(--ink)}
.bg-dark{background:linear-gradient(135deg,#2b2b2b,#151515)}
.bg-yellow{background:linear-gradient(135deg,#f6c51c,#d9a912)}
.bg-gray{background:linear-gradient(135deg,#e4e4e4,#cfcfcf)}

/* dark band */
.darkband{position:absolute;left:0;top:1619px;width:1200px;height:1628px}
.darkband__bg{background:linear-gradient(180deg,#262626 0%,#1d1d1d 40%,#232323 70%,#1a1a1a 100%)}
.circle-photo{left:141px;top:1699px;width:336px;height:336px;border-radius:50%;background:radial-gradient(circle at 40% 35%,#cfd8e0,#6b8aa3 55%,#3a4a57)}
.software-label{left:132px;top:1875px;font-size:24px;font-weight:700;color:var(--paper)}
.why__title{left:680px;top:1724px;font-size:26px;font-weight:700;color:var(--paper)}
.why__list{left:672px;top:1800px;width:350px;list-style:none}
.why__list li{position:relative;padding-left:27px;font-size:12.5px;line-height:20px;color:var(--paper);margin-bottom:16px}
.why__list svg{position:absolute;left:0;top:3px}
.rule{position:absolute;left:122px;width:956px;height:1px;background:rgba(255,255,255,.22)}
.software__ghost{left:136px;top:2205px;font-size:64px}
.software__text{left:135px;top:2302px;width:358px;font-size:12.5px;line-height:20px;color:var(--paper)}
.store{position:absolute;top:2406px;height:40px;background:var(--ink);display:flex;align-items:center;gap:8px;padding:0 10px;color:var(--paper);white-space:nowrap}
.store small{display:block;font-size:9px;line-height:1}
.store strong{display:block;font-size:12.5px;font-weight:600;line-height:1.3}
.laptop{left:565px;top:2172px;width:530px;height:293px;background:linear-gradient(180deg,#3b4b70 0%,#e9edf4 30%,#f4f6fa 80%,#9aa0a8 100%);border-radius:6px}
.guarantee__ghost{left:0;width:1200px;text-align:center;top:2633px;font-size:72px;-webkit-text-stroke:1.5px rgba(255,255,255,.09)}
.center-title{position:absolute;left:0;width:1200px;text-align:center;font-size:27px;font-weight:700;color:var(--paper)}
.guarantee__line{position:absolute;left:0;width:1200px;text-align:center;font-size:14px;color:var(--paper)}
.big{font-size:50px;font-weight:700;color:var(--yellow);vertical-align:-6px;line-height:1}
.partners__ghost{left:0;width:1200px;text-align:center;top:3010px;font-size:70px;-webkit-text-stroke:1.5px rgba(255,255,255,.09)}
.partners{left:63px;top:3120px;width:1068px;display:flex;justify-content:space-between;align-items:center;color:var(--paper);font-size:17px;font-weight:500}

/* contact */
.contact{position:absolute;left:0;top:3247px;width:1200px;height:538px;background:linear-gradient(90deg,#ffffff 0%,#f6f6f6 50%,#eceeef 100%)}
.contact__photo{left:560px;top:0;width:640px;height:538px;background:linear-gradient(120deg,#f1f2f3 0%,#dfe5ec 45%,#9fb6cf 70%,#2f3a4a 100%)}
.contact__ghost{left:62px;top:70px;font-size:62px}
.field{position:absolute;left:67px;width:376px;background:var(--field);border:1px solid var(--field-line);font-size:12px;color:var(--muted);padding:9px 9px}
.send{position:absolute;left:67px;top:424px;width:135px;height:39px;background:var(--ink);color:var(--paper);font-size:13px;font-weight:700;display:flex;align-items:center;justify-content:center}

/* footer */
.footer{position:absolute;left:0;top:3785px;width:1200px;height:522px;overflow:hidden}
.footer__bg{background:linear-gradient(180deg,#f8c71d 0%,#efbd18 55%,#e5b216 100%)}
.footer__brand{left:0;width:1200px;text-align:center;top:96px;font-size:22px;color:var(--paper)}
.footer__nav{left:254px;width:692px;top:174px;display:flex;justify-content:center;gap:18px;font-size:11px;color:var(--ink);font-weight:500}
.footer__rule{left:254px;width:692px;top:205px;height:1px;background:rgba(0,0,0,.35)}
.f-item{position:absolute;top:238px;display:flex;align-items:center;gap:16px;font-size:11.5px;line-height:18px;color:var(--ink)}
.f-icon{width:32px;height:32px;border-radius:50%;background:var(--ink);display:flex;align-items:center;justify-content:center;flex:none}
.footer__heading{left:20px;top:312px;font-size:28px;font-weight:700;color:var(--ink);white-space:nowrap;line-height:1.2}
.social{left:532px;top:330px;display:flex;gap:5px}
.social span{width:28px;height:28px;border-radius:50%;border:1.5px solid var(--ink)}
.copyright{left:60px;top:365px;font-size:11px;color:var(--ink)}
.note{left:90px;width:1020px;top:411px;text-align:center;font-size:11.5px;line-height:19px;color:var(--ink)}
</style>
</head>
<body>

<section class="hero">
  <div class="hero__topwhite"></div>
  <div class="hero__yellow"></div>
  <div class="abs brand header__brand">VANTOR 3PL</div>
  <div class="abs header__call">
    <div class="call__icon">
      <svg width="16" height="16" viewBox="0 0 24 24"><path fill="#1b1b1b" d="M6.6 10.8a15.1 15.1 0 0 0 6.6 6.6l2.2-2.2c.3-.3.7-.4 1-.2 1.1.4 2.3.6 3.6.6.6 0 1 .4 1 1V20c0 .6-.4 1-1 1A17 17 0 0 1 3 4c0-.6.4-1 1-1h3.5c.6 0 1 .4 1 1 0 1.300.2 2.5.6 3.6.1.3 0 .7-.2 1z"/></svg>
    </div>
    <div><div class="call__label">CALL :</div><div class="call__number">+123 456 7890</div></div>
  </div>
  <div class="abs menu"><span></span><span></span><span></span></div>
  <div class="abs hero__photo" role="img" aria-label="Shipping containers, a cargo truck and a plane against a sunset sky"></div>
  <div class="abs hero__kicker">VANTOR 3PL</div>
  <h1 class="abs hero__title">WE MAKE YOUR<br>LOGISTIC SIMPLE</h1>
  <p class="abs hero__text">Vantor 3PL is your one stop 3PL that will help you grow your business and allow you to be hands off. We offer high end services and meet our commitment, guaranteed.</p>
  <a class="btn btn--light">GET A QUOTE</a>
  <a class="btn btn--dark">CONTACT US</a>
  <div class="abs hero__pager" style="top:455px">P<br>R<br>E<br>V</div>
  <div class="abs hero__pager" style="top:537px">N<br>E<br>X<br>T</div>
</section>

<section class="benefit">
  <div class="ghost benefit__ghost">BENIFIT</div>
  <h2 class="abs benefit__title">BENIFIT 3PL</h2>
  <p class="abs benefit__sub">WE SOLVE YOUR LOGISTIC PROBLEM</p>

  <div class="tile" style="left:900px;top:83px">
    <div class="img-fill bg-dark" role="img" aria-label="Warehouse worker with parcels"></div>
    <div class="tile__num">01</div><p class="tile__text">48 hour turn around guarantee</p>
  </div>
  <div class="tile" style="left:0;top:382px">
    <div class="img-fill bg-gray" role="img" aria-label="Faded warehouse shelving"></div>
    <p class="tile__intro">Vantor 3PL is your one stop 3PL that will help you grow your business and allow you to be hands off. We offer high end services and meet our commitment, guaranteed.</p>
  </div>
  <div class="tile" style="left:600px;top:382px">
    <div class="img-fill bg-dark" role="img" aria-label="Desk with laptop and documents"></div>
    <div class="tile__num">02</div><p class="tile__text">No monthly subscription</p>
  </div>
  <div class="tile tile--yellow" style="left:900px;top:382px">
    <div class="img-fill bg-yellow" role="img" aria-label="Office worker holding folders"></div>
    <div class="tile__num">03</div><p class="tile__text">No receiving fees</p>
  </div>
  <div class="tile tile--yellow" style="left:300px;top:682px">
    <div class="img-fill bg-yellow" role="img" aria-label="Stacked pallets in a warehouse"></div>
    <div class="tile__num">04</div><p class="tile__text">No pallet or outbound fees</p>
  </div>
  <div class="tile tile--wide" style="left:600px;top:682px">
    <div class="img-fill bg-dark" role="img" aria-label="Hands using a phone next to a coffee cup"></div>
    <div class="tile__num" style="left:52px">05</div><p class="tile__text" style="left:52px">Email and phone support</p>
  </div>
</section>

<section class="darkband">
  <div class="img-fill darkband__bg" role="img" aria-label="Dim background of trucks at a loading yard"></div>
</section>

<div class="abs circle-photo" role="img" aria-label="Container truck inside a round frame"></div>
<div class="abs software-label">OUR SOFTWARE</div>
<h2 class="abs why__title">WHY USE A PREP 3PL</h2>
<ul class="abs why__list">
  <li><svg width="15" height="15" viewBox="0 0 16 16"><circle cx="8" cy="8" r="6.5" fill="none" stroke="#f8c71d" stroke-width="2"/><circle cx="8" cy="8" r="2.3" fill="#f8c71d"/></svg>Work from anywhere in the world.</li>
  <li><svg width="15" height="15" viewBox="0 0 16 16"><circle cx="8" cy="8" r="6.5" fill="none" stroke="#f8c71d" stroke-width="2"/><circle cx="8" cy="8" r="2.3" fill="#f8c71d"/></svg>Don't have to manage employees, health insurance plans, payroll, sick calls, etc.</li>
  <li><svg width="15" height="15" viewBox="0 0 16 16"><circle cx="8" cy="8" r="6.5" fill="none" stroke="#f8c71d" stroke-width="2"/><circle cx="8" cy="8" r="2.3" fill="#f8c71d"/></svg>Don't get locked into a 3-5 year warehouse lease where you guarantee hundreds of thousands of dollars</li>
  <li><svg width="15" height="15" viewBox="0 0 16 16"><circle cx="8" cy="8" r="6.5" fill="none" stroke="#f8c71d" stroke-width="2"/><circle cx="8" cy="8" r="2.3" fill="#f8c71d"/></svg>Grow your business without commitment</li>
</ul>
<div class="rule" style="top:2094px"></div>

<div class="ghost ghost--light software__ghost">SOFTWARE</div>
<p class="abs software__text">Know what inventory is at our warehouse in real time. Our software allows you to track your inventory and know how your shipment status in real time. Professional software designed specifically for our needs.</p>
<div class="store" style="left:135px;width:136px">
  <svg width="18" height="18" viewBox="0 0 20 20"><polygon points="4,2 17,10 4,18" fill="#f8c71d"/></svg>
  <div><small>get it on</small><strong>Appvane</strong></div>
</div>
<div class="store" style="left:292px;width:150px">
  <svg width="16" height="16" viewBox="0 0 20 20"><circle cx="10" cy="10" r="7" fill="#ffffff"/></svg>
  <div><small>Download on the</small><strong>Orchard Store</strong></div>
</div>
<div class="abs laptop" role="img" aria-label="Laptop showing the inventory dashboard, flanked by line drawings of a truck, plane and ship"></div>
<div class="rule" style="top:2557px"></div>

<div class="ghost guarantee__ghost">GUARANTEE</div>
<h2 class="center-title" style="top:2650px">GUARANTEE</h2>
<p class="guarantee__line" style="top:2730px">All orders will be prepped and ready for shipment in <span class="big">48</span> business hours (often 24 or less)</p>
<p class="guarantee__line" style="top:2801px">and we guarantee it. We are confident in our services and if we do not fulfill our obligation, we</p>
<p class="guarantee__line" style="top:2836px">offer a <span class="big">500</span> item (up to $700) credit on your next shipment.</p>
<div class="rule" style="top:2946px"></div>

<div class="ghost partners__ghost">PARTNERS</div>
<h2 class="center-title" style="top:3026px">PARTNERS</h2>
<div class="abs partners">
  <span>Nordweave</span><span>Brindlemart</span><span>Cobalt Sky</span><span>Meridian Cloud</span><span>Velqora</span><span>Crimsonline</span><span>Harborbox</span>
</div>

<section class="contact">
  <div class="abs contact__photo" role="img" aria-label="Smiling businessman holding a laptop in front of a large company sign"></div>
  <div class="ghost contact__ghost">CONTACT US</div>
  <div class="field" style="top:157px;height:35px">Name :</div>
  <div class="field" style="top:210px;height:35px">Email :</div>
  <div class="field" style="top:262px;height:35px">Phone :</div>
  <div class="field" style="top:316px;height:88px">Message :</div>
  <a class="send">SEND MESSAGE</a>
</section>

<footer class="footer">
  <div class="img-fill footer__bg" role="img" aria-label="Yellow tinted shipping containers"></div>
  <div class="abs brand footer__brand">VANTOR 3PL</div>
  <nav class="abs footer__nav">
    <span>HOME</span><span>|</span><span>WHO WE ARE</span><span>|</span><span>WHY US</span><span>|</span><span>BENIFIT</span><span>|</span><span>SOFTWARE</span><span>|</span><span>GUARANTEE</span>
  </nav>
  <div class="abs footer__rule"></div>
  <div class="f-item" style="left:287px">
    <div class="f-icon"><svg width="14" height="16" viewBox="0 0 14 18"><path fill="#f8c71d" d="M7 0a7 7 0 0 0-7 7c0 5 7 11 7 11s7-6 7-11a7 7 0 0 0-7-7zm0 9.5A2.5 2.5 0 1 1 7 4.5a2.5 2.5 0 0 1 0 5z"/></svg></div>
    <span>101- Lorem ipsum is dummy<br>printing text</span>
  </div>
  <div class="f-item" style="left:556px">
    <div class="f-icon"><svg width="15" height="12" viewBox="0 0 16 12"><rect x="0.5" y="0.5" width="15" height="11" fill="#f8c71d"/><path d="M1 1l7 6 7-6" fill="none" stroke="#1b1b1b" stroke-width="1.4"/></svg></div>
    <span>info@vantor3pl.com</span>
  </div>
  <div class="f-item" style="left:789px">
    <div class="f-icon"><svg width="14" height="14" viewBox="0 0 24 24"><path fill="#f8c71d" d="M6.6 10.8a15.1 15.1 0 0 0 6.6 6.6l2.2-2.2c.3-.3.7-.4 1-.2 1.1.4 2.3.6 3.6.6.6 0 1 .4 1 1V20c0 .6-.4 1-1 1A17 17 0 0 1 3 4c0-.6.4-1 1-1h3.5c.6 0 1 .4 1 1 0 1.3.2 2.5.6 3.6.1.3 0 .7-.2 1z"/></svg></div>
    <span>123 456 7890</span>
  </div>
  <div class="abs footer__heading">CONTACT US</div>
  <div class="abs social"><span></span><span></span><span></span><span></span></div>
  <p class="abs copyright">©VANTOR 3PL - 2021 .All Right Reserved</p>
  <p class="abs note">*Our guarantee is 48 hours from the time an outbound shipment is created in our system. Weekends and holidays excluded. Orders created on a Friday after hours, Saturday or Sunday will be counted from the open of business on Monday morning. We offer a credit of up to 500 units on your next shipment. These credits are for standard prep items only, no bundles, bubble wrapped or multipack units. Outbound shipments will be prepped and ready to ship. We are unable to control shipping companies and freight carriers. Orders after daily pickups are completed will be ready for next day pickup.</p>
</footer>

</body>
</html>
```